Business Card Design needed for logo design project

Our company needs a Business Card Design. Please refer to our original project in the link above.
Dorian Pellworth
Broker

W: Velvetcrestestates.example
P: 555-302-7184
F: 555-741-2096
E: dorianpellworth@mailbox.example
A: North Dallas Office
Updates

Name Spelling update , sorry Dorian Pellworth card is double sided

```html
<!DOCTYPE html>
<html lang="en">
<head>
<meta charset="utf-8">
<title>Velvetcrest Estates – Business Card</title>
<link rel="stylesheet" href="https://fonts.googleapis.com/css2?family=Cinzel:wght@400;600&family=Cormorant+Garamond:ital,wght@0,400;0,500;1,400&display=swap">
<style>
  :root {
    --backdrop: #3b3b3b;
    --card-black: #121212;
    --card-black-soft: #1e1e1e;
    --card-white: #fbfbf9;
    --gold: #b8955a;
    --gold-light: #d2b27a;
    --green: #2fae6a;
    --text-light: #f2f2f2;
  }
  * { margin: 0; padding: 0; box-sizing: border-box; }
  html, body {
    width: 1200px; height: 1023px; overflow: hidden;
    background: var(--backdrop);
  }
  .sheet {
    width: 1200px; height: 1023px;
    display: flex; flex-direction: column;
    align-items: center; justify-content: center; gap: 56px;
  }
  .card {
    width: 720px; height: 411px;
    border: 3px solid var(--gold);
    border-radius: 4px;
    overflow: hidden;
    position: relative;
    box-shadow: 0 14px 30px rgba(0,0,0,0.45);
  }

  /* Back side: contact details + brand panel */
  .card-back { display: flex; }
  .contact-panel {
    flex: 0 0 58%;
    background: linear-gradient(160deg, var(--card-black-soft), var(--card-black));
    padding: 58px 0 0 56px;
    color: var(--text-light);
  }
  .person-name {
    font-family: "Cormorant Garamond", serif;
    font-weight: 400; font-size: 38px; letter-spacing: 0.5px;
  }
  .person-role {
    font-family: "Cormorant Garamond", serif;
    font-style: italic; font-size: 30px;
    color: var(--green);
    margin: 2px 0 0 100px;
  }
  .contact-list { list-style: none; margin-top: 34px; }
  .contact-item {
    display: flex; align-items: center; gap: 14px;
    font-family: "Cormorant Garamond", serif;
    font-size: 21px; line-height: 1; margin-bottom: 14px;
  }
  .contact-icon {
    width: 22px; height: 22px; flex: 0 0 22px;
    border-radius: 4px; background: var(--green);
    display: flex; align-items: center; justify-content: center;
  }
  .contact-icon svg { width: 14px; height: 14px; }

  .brand-panel {
    flex: 1;
    background: var(--card-white);
    display: flex; flex-direction: column;
    align-items: center; justify-content: center; gap: 18px;
  }

  /* Brand lockup */
  .brand-mark {
    width: 56px; height: 56px; border-radius: 50%;
    background: var(--gold);
  }
  .brand-name {
    font-family: "Cinzel", serif; font-weight: 600;
    color: var(--gold); font-size: 28px;
    text-align: center; line-height: 1.25; letter-spacing: 1px;
  }

  /* Front side */
  .card-front {
    background: linear-gradient(160deg, var(--card-black-soft), var(--card-black));
    display: flex; align-items: center; justify-content: center; gap: 34px;
  }
  .card-front .brand-mark { width: 110px; height: 110px; }
  .card-front .brand-name { font-size: 40px; text-align: left; }
</style>
</head>
<body>
<main class="sheet">

  <section class="card card-back" aria-label="Card back">
    <div class="contact-panel">
      <h1 class="person-name">Dorian Pellworth</h1>
      <p class="person-role">Broker</p>
      <ul class="contact-list">
        <li class="contact-item">
          <span class="contact-icon"><svg viewBox="0 0 14 14"><rect x="1.5" y="3" width="11" height="8" fill="none" stroke="#fff" stroke-width="1.4"/><path d="M1.5 3 L7 8 L12.5 3" fill="none" stroke="#fff" stroke-width="1.4"/></svg></span>
          dorianpellworth@mailbox.example
        </li>
        <li class="contact-item">
          <span class="contact-icon"><svg viewBox="0 0 14 14"><rect x="4" y="1.5" width="6" height="11" rx="1" fill="none" stroke="#fff" stroke-width="1.4"/><circle cx="7" cy="10.5" r="0.8" fill="#fff"/></svg></span>
          555-302-7184
        </li>
        <li class="contact-item">
          <span class="contact-icon"><svg viewBox="0 0 14 14"><rect x="2" y="5" width="10" height="7" rx="1" fill="none" stroke="#fff" stroke-width="1.4"/><path d="M3 5 Q7 0.5 11 5" fill="none" stroke="#fff" stroke-width="1.4"/><circle cx="7" cy="8.5" r="1.5" fill="#fff"/></svg></span>
          555-741-2096
        </li>
        <li class="contact-item">
          <span class="contact-icon"><svg viewBox="0 0 14 14"><circle cx="7" cy="7" r="5.5" fill="none" stroke="#fff" stroke-width="1.3"/><ellipse cx="7" cy="7" rx="2.4" ry="5.5" fill="none" stroke="#fff" stroke-width="1.1"/><line x1="1.5" y1="7" x2="12.5" y2="7" stroke="#fff" stroke-width="1.1"/></svg></span>
          Velvetcrestestates.example
        </li>
      </ul>
    </div>
    <div class="brand-panel">
      <span class="brand-mark" aria-hidden="true"></span>
      <p class="brand-name">Velvetcrest<br>Estates</p>
    </div>
  </section>

  <section class="card card-front" aria-label="Card front">
    <span class="brand-mark" aria-hidden="true"></span>
    <p class="brand-name">Velvetcrest<br>Estates</p>
  </section>

</main>
</body>
</html>
```